Project Report for American Indian and Alaska Native org (U.S.)

We need a report formatted/ design / layout.
We are a nonprofit organization that works on indigenous elder issues.
The report should reflect our logo color scheme.
Body font should be at least 11 point sans serif.
Ideally, headings and title would use fonts that are reminiscent of tribal cultures though not hard to read or whimsical/ unprofessional looking.

We have used some light script style fonts in the past -- nothing too cursive looking though.

The audience is public health professionals and tribal staff and leadership.

We want our organization's logo (QV7) and the project logo (brain health) incorporated into the title page.

We prefer the files to come back to us in an editable fashion + a pdf file.

Industry/Entity Type

tribal communities and public health officials

Font styles to use
Serif
Sans Serif

Requirements
Must have
• our logo and color scheme
Should not have
• headdress images

```html
<!DOCTYPE html>
<html lang="en">
<head>
<meta charset="utf-8">
<title>Background – Report Spread</title>
<link href="https://fonts.googleapis.com/css2?family=Arimo:ital,wght@0,400;0,700;1,400&family=Bungee&display=swap" rel="stylesheet">
<style>
  :root{
    --teal:#4a9ea7;
    --red:#b4524a;
    --ink:#1f1f1f;
    --purple:#4a2a6a;
    --panel:#e7e7ea;
    --paper:#ffffff;
  }
  *{box-sizing:border-box;margin:0;padding:0}
  html,body{width:1200px;height:424px;overflow:hidden;background:var(--paper)}
  body{position:relative;font-family:"Arimo",Arial,sans-serif;color:var(--ink)}
  .abs{position:absolute}

  .section-band{position:absolute;top:43px;height:53px;width:171px;
    background:linear-gradient(180deg,var(--teal) 0%,var(--red) 100%);
    display:flex;align-items:center;justify-content:center}
  .section-band h1{font-family:"Bungee",sans-serif;font-weight:400;color:#fff;font-size:16.5px;letter-spacing:0}
  .band-left{left:0}
  .band-right{left:1029px}

  .rule{position:absolute;height:1.6px}
  .rule.red{background:var(--red)}
  .rule.teal{background:var(--teal)}
  .vrule{position:absolute;width:1.6px}
  .vrule.red{background:var(--red)}
  .vrule.teal{background:var(--teal)}

  .body-copy{font-size:7.9px;line-height:9.4px}
  .body-copy p{margin-bottom:4px}
  .link{color:var(--teal)}

  .section-head{position:absolute;text-align:center;font-family:"Bungee",sans-serif;font-weight:400;color:var(--teal);
    font-size:11px;line-height:12px;letter-spacing:.2px}
  .section-head span{display:inline-block;transform:skewX(-12deg)}

  .figure-caption{left:44px;top:119px;width:80px;font-size:7.3px;line-height:8.6px;font-style:italic}
  .figure-caption .fig-no{color:var(--red)}

  .figure-panel{left:44px;top:168px;width:279px;height:194px;background:var(--panel);padding:17px 10px 6px 16px}
  .figure-mark{position:absolute;left:8px;top:18px;width:35px;height:35px;border-radius:50%;background:var(--purple)}
  .figure-title{margin-left:32px;font-size:6.6px;font-weight:700;color:var(--purple);margin-bottom:2px}
  .figure-intro{margin-left:32px;font-size:4.1px;line-height:5.4px;margin-bottom:9px}
  .figure-cols{display:flex;gap:12px}
  .figure-col{flex:1}
  .figure-col h3{font-size:4.5px;font-weight:700;margin-bottom:5px}
  .figure-col ol{list-style:none}
  .figure-col li{font-size:4.1px;line-height:5.5px;padding-left:8px;text-indent:-8px;margin-bottom:5px}
  .figure-col li span{display:inline-block;width:8px;text-indent:0}

  .quote{font-style:italic;margin:9px 0 4px 20px}
  .cite{text-align:right}

  .page-no{font-family:"Arimo",sans-serif;font-weight:700;font-size:12px;top:373px}
  .org-name{position:absolute;top:371px;display:flex;align-items:center;gap:6px;color:var(--red);font-weight:700;font-size:9px;line-height:10.5px;text-transform:uppercase}
  .org-name .dot{width:10px;height:10px;border-radius:50%;background:var(--red);flex:none}
</style>
</head>
<body>

<!-- Left page -->
<div class="section-band band-left"><h1>Background</h1></div>
<div class="rule red" style="left:172px;top:50px;width:376px"></div>
<div class="rule teal" style="left:172px;top:55px;width:382px"></div>
<div class="vrule teal" style="left:552px;top:55px;height:292px"></div>
<div class="rule teal" style="left:333px;top:345px;width:221px"></div>
<div class="vrule red" style="left:139px;top:98px;height:61px"></div>
<div class="vrule teal" style="left:144px;top:98px;height:61px"></div>

<div class="abs body-copy" style="left:184px;top:67px;width:358px">
  <p>called for a National Plan for ADRD that would include input from an Advisory Council (also established by law). The Council also advises the Department of Community Wellness (DCW) on priorities for program changes. The first National Plan has been updated annually since its creation in 2012 (Office of Policy Review, 2020).</p>
  <p>The CARE Network for Memory Health Act, passed into law on December 31, 2018 (P.L. 09-214), amends the Community Health Services Act (Section 41B; Title 12, Part 7). The activities outlined in CARE are designed to create a uniform national public health infrastructure focusing on issues such as increasing early detection and diagnosis, risk reduction, prevention of avoidable hospitalizations, and supporting dementia caregiving.</p>
</div>

<div class="abs figure-caption"><span class="fig-no">Figure 2.</span><br>Bright Minds Initiative’s Tribal Pathway Guide Public Health Strategies</div>

<div class="abs figure-panel">
  <div class="figure-mark" role="img" aria-label="Round emblem with three feathers"></div>
  <div class="figure-title">PUBLIC HEALTH ACTIONS TO CARE FOR AN AGING POPULATION</div>
  <div class="figure-intro">The Bright Minds Initiative’s <i>Tribal Pathway Guide</i> is tailored for leaders of American Indian and Alaska Native (AI/AN) communities as they develop a broad response to Alzheimer’s and other dementias. The following eight public health strategies can inform and shape that response. Tribal leaders are encouraged to discuss these strategies with their community and involve members in planning and implementing these community-wide approaches.</div>
  <div class="figure-cols">
    <div class="figure-col">
      <h3>EDUCATE AND EMPOWER COMMUNITY MEMBERS</h3>
      <ol>
        <li><span>1.</span>Work with community members to understand brain health, early warning signs of dementia, and benefits of early detection and diagnosis for persons with dementia and their caregivers.</li>
        <li><span>2.</span>Encourage community members to use effective interventions, best practices, and traditional wellness practices to protect brain health, address cognitive impairment, and support persons with dementia and their caregivers.</li>
        <li><span>3.</span>Provide information and tools to help older adults with dementia and their caregivers anticipate and respond to challenges that typically arise during the course of dementia.</li>
        <li><span>4.</span>Promote engagement among tribal leaders in dementia issues by offering information and education on the basics of cognitive health and impairment, the impact of dementia on caregivers and communities, and the role of public health approaches in addressing this priority problem.</li>
      </ol>
    </div>
    <div class="figure-col">
      <h3>COLLECT AND USE DATA</h3>
      <ol>
        <li><span>5.</span>Support collection and use of local data on dementia and caregiving in AI/AN communities to plan programs and approaches.</li>
        <li><span>6.</span>Promote the inclusion of healthcare quality measures that address both cognitive assessments and the delivery of care to AI/ANs with dementia.</li>
      </ol>
      <h3>STRENGTHEN THE WORKFORCE</h3>
      <ol>
        <li><span>7.</span>Educate healthcare and aging services professionals in tribal nations about the signs and symptoms of dementia and about caregiving for persons with dementia.</li>
        <li><span>8.</span>Educate healthcare and aging services professionals on the best ways to support families and caregivers of older adults with dementia.</li>
      </ol>
    </div>
  </div>
</div>

<div class="section-head" style="left:333px;top:160px;width:210px"><span>Tribal Pathway Guide</span></div>
<div class="abs body-copy" style="left:333px;top:175px;width:210px">
  <p>The <span class="link">Bright Minds Initiative's Tribal Pathway Guide</span>, published in 2019, is the first-ever public health guide focused on dementia in American Indian and Alaska Native (AI/AN) communities (Centers for Community Health Prevention (CCHP)). The Tribal Pathway Guide identified eight specific public health strategies for tribal communities (Figure 2). It is intended as a tool for leaders of the nation's 574 federal and state-recognized tribes to engage their communities in addressing this vital issue. Strategy four explicitly acknowledges the importance of the engagement of tribal leaders. These leaders include tribal officials, tribal health and aging services professionals, and regional tribal health organizational leaders. A scan of U.S. tribal policies, laws, and plans regarding ADRD issues is a natural extension of previous U.S.-based efforts and a starting point for identifying critical information resources for tribal leaders.</p>
</div>

<!-- Left footer -->
<div class="rule teal" style="left:0;top:377px;width:25px;height:2.4px"></div>
<div class="rule red" style="left:0;top:385px;width:25px;height:2.4px"></div>
<div class="abs page-no" style="left:32px">6</div>
<div class="rule teal" style="left:48px;top:377px;width:355px;height:2.4px"></div>
<div class="rule red" style="left:48px;top:385px;width:355px;height:2.4px"></div>
<div class="org-name" style="left:414px"><span class="dot"></span><span>QV7 International Network<br>for Elder Wellbeing</span></div>

<!-- Right page -->
<div class="section-band band-right"><h1>Background</h1></div>
<div class="rule red" style="left:650px;top:50px;width:379px"></div>
<div class="rule teal" style="left:646px;top:55px;width:383px"></div>
<div class="vrule teal" style="left:646px;top:55px;height:292px"></div>
<div class="rule teal" style="left:646px;top:345px;width:409px"></div>
<div class="vrule teal" style="left:1053px;top:95px;height:252px"></div>
<div class="vrule red" style="left:1058px;top:95px;height:243px"></div>

<div class="section-head" style="left:653px;top:67px;width:358px"><span>Tribal Sovereignty</span></div>
<div class="abs body-copy" style="left:653px;top:82px;width:360px">
  <p>The U.S. Constitution acknowledges federally recognized Indian tribes as distinct governments. They have, with few exceptions, the same powers as state governments to regulate their internal affairs. Sovereignty for tribes includes the right to establish their own form of government, determine membership requirements, enact legislation, and establish law enforcement and court systems.</p>
  <p>Federally recognized tribal nations and their leadership have the power, duty, and obligation to promote the health and well-being of their citizens (Harlow, 2000). Based upon powers of sovereignty, they are the de facto public health entities for their citizens. According to the National Tribal Wellness Board (NTWB, n.d.), tribal public health is underrepresented or overlooked within the current U.S. health system. Tribal communities are rebuilding and defining their public health systems, having developed them at a different pace than other public health systems in the U.S. Current tribal systems often differ in structure, infrastructure, scale, and scope from state and local public health entities, if they exist at all. The current state of tribal public health systems is the result of chronic underfunding, federal and state policy, epidemics, and a long-standing history of colonialism, according to NTWB.</p>
  <p>American Indian and Alaska Native people are U.S. Citizens and generally subject to federal, state, and local law. However, on federal Indian reservations, only federal and tribal laws apply to members of the tribe unless Congress specifically provides otherwise (Office of Tribal Relations). With this in mind, we sought to identify existing tribal laws, policies, and plans regarding dementia and then look at state actions that impact tribes.</p>
  <p class="quote">As sovereign nations, tribes are uniquely situated to use law as a public health tool to promote the health and well-being of their communities. Additionally, federal law creates a framework that governs the relationships among tribes, states, and the federal government that can affect tribal public health.</p>
  <p class="cite">Centers for Community Health Prevention (2017)</p>
</div>

<!-- Right footer -->
<div class="org-name" style="left:648px"><span class="dot"></span><span>QV7 International Network<br>for Elder Wellbeing</span></div>
<div class="rule teal" style="left:795px;top:377px;width:356px;height:2.4px"></div>
<div class="rule red" style="left:795px;top:385px;width:356px;height:2.4px"></div>
<div class="abs page-no" style="left:1157px">7</div>
<div class="rule teal" style="left:1173px;top:377px;width:27px;height:2.4px"></div>
<div class="rule red" style="left:1173px;top:385px;width:27px;height:2.4px"></div>

</body>
</html>
```